Word Template Designs for Offensive Security Professional Services Report

We need a Microsoft Word Template designed for our Offensive Security professional services reports which includes the following services:

RedTeaming
Network Penetration Testing
Web Application Penetration Testing
Wireless Penetration Testing
Social Engineering

The templates should include the following:
Cover Page design with our Logo included
Executive Summary Page design
Detailed Findings Page design
Design for Last Page

Lastly, I would also like a template I can use for all of my Statements of Work

Requirements
Must have
• Beautiful Eye Catching HD pictures that represent my Offensive Security projects
The design should flow well with our logo

```html
<!DOCTYPE html>
<html lang="en">
<head>
<meta charset="utf-8">
<title>Penetration Test Report Template – Page Spread</title>
<link href="https://fonts.googleapis.com/css2?family=Roboto:wght@400;500;700&display=swap" rel="stylesheet">
<style>
:root{
  --olive:#9db548;
  --olive-box:#a9bf5e;
  --ink:#222;
  --muted:#555;
  --rule:#bbb;
  --board:#dcdcdc;
  --dark:#14181c;
  --red:#c4161c;
  --critical:#6a3d8f;
  --high:#d21f1f;
  --medium:#e0812a;
  --low:#3a8fd0;
  --info:#8dbb3c;
  --bar:#8c8c8c;
}
*{box-sizing:border-box;margin:0;padding:0}
html,body{width:1200px;height:921px;overflow:hidden;background:var(--board);font-family:"Roboto",Arial,sans-serif;color:var(--ink)}
.board{position:relative;width:1200px;height:921px;background:var(--board)}
.page{position:absolute;width:226px;height:293px;background:#fff;overflow:hidden;box-shadow:0 0 2px rgba(0,0,0,.15)}
.c1{left:11px}.c2{left:248px}.c3{left:485px}.c4{left:722px}.c5{left:959px}
.r1{top:11px}.r2{top:314px}.r3{top:617px}

/* footer */
.foot{position:absolute;left:0;bottom:0;width:226px;height:60px}
.bar{position:absolute;left:26px;right:0;bottom:0;height:4px;background:var(--bar)}
.pnum{position:absolute;left:40px;bottom:9px;font-size:5px;color:var(--olive)}
.brand{position:absolute;right:10px;bottom:10px;display:flex;align-items:center;gap:2px}
.brand .mark{width:9px;height:9px;border-radius:50%;background:#3a3f3a}
.brand .name{font-size:5.2px;font-weight:700;color:var(--olive);white-space:nowrap}

/* text */
.txt{position:absolute;left:26px;width:174px;font-size:3.1px;line-height:1.3;color:#333;text-align:justify}
.txt p{margin-bottom:3px}
.txt b{color:#111}
.hbox{position:absolute;background:var(--olive-box);color:#fff;font-size:7px;line-height:1.05;padding:1px 3px;font-weight:500}
.hbox span{color:#1c1c1c}
.photo{position:absolute}

/* confidential */
.stop{position:absolute;top:121px;width:100%;text-align:center;color:var(--red);font-size:9px;font-weight:700;letter-spacing:1.5px}
.conf{position:absolute;top:143px;left:42px;width:142px;border-top:.6px solid #333;border-bottom:.6px solid #333;text-align:center;font-size:6px;font-weight:500;padding:2px 0}
.conf-txt{position:absolute;top:156px;left:42px;width:142px;font-size:4px;line-height:1.45;text-align:justify;font-variant:small-caps;color:#222}
.conf-txt em{font-style:normal;color:var(--red);font-weight:700}
.conf-txt p{margin-bottom:4px}
.mini-brand{position:absolute;top:254px;left:0;width:100%;display:flex;justify-content:center;align-items:center;gap:2px}
.mini-brand .mark{width:10px;height:10px;border-radius:50%;background:#3a3f3a}
.mini-brand .name{font-size:4.4px;font-weight:700;color:var(--olive)}

/* toc */
.toc-head{position:absolute;top:101px;right:31px;background:var(--olive-box);color:#fff;font-size:7px;text-align:center;letter-spacing:.8px;padding:1px 3px;line-height:1.15}
.toc-head span{color:#1c1c1c}
.toc-rule{position:absolute;top:108px;left:34px;width:30px;height:.6px;background:#777}
.toc{position:absolute;top:121px;left:34px;width:160px;font-size:3.2px;line-height:1.72;list-style:none}
.toc li{display:flex}
.toc li .d{flex:1;border-bottom:.4px dotted #666;margin:0 1px 1.2px}
.toc li.sub{padding-left:6px;font-variant:small-caps}
.toc li.sub2{padding-left:3px;font-variant:small-caps}

/* tables */
table{border-collapse:collapse;font-size:2.9px;color:#333}
.tbl-sum{position:absolute;top:88px;left:26px;width:174px;line-height:1.2}
.tbl-sum th{border-bottom:.5px solid #333;border-top:.5px solid #333;text-align:center;font-weight:500;padding:.4px}
.tbl-sum td{padding:.6px 2px;text-align:center;height:5.2px}
.tbl-sum td:first-child{text-align:left;padding-left:3px}
.sw{display:inline-block;width:3px;height:3px}
.tbl-def{position:absolute;top:160px;left:26px;width:174px}
.tbl-def th{text-align:left;border-bottom:.5px solid #333;font-weight:500;padding:.5px 2px}
.tbl-def td{border-bottom:.4px solid #ccc;padding:1px 2px;vertical-align:middle;line-height:1.25}
.tbl-def td:first-child{width:40px;font-weight:700;color:#111;white-space:nowrap}

/* findings */
.find{position:absolute;left:26px;width:174px}
.find .hbox{position:relative;display:inline-block}
.find .sub{font-size:3.6px;font-weight:700;margin:1.5px 0 1px 3px}
.find .sub i{font-style:normal}
.find .rule{height:1px;margin-bottom:1px}
.find .row{font-size:3px;line-height:1.3;border-bottom:.4px solid #bbb;padding:1px 2px;text-align:justify;color:#333}
.find .row b{color:#111}
.find .row a{color:#2440c8;text-decoration:underline}
.find .end{height:1px}

/* methodology */
.meth-h{position:absolute;left:26px;font-size:4px;font-weight:700;display:flex;align-items:center;gap:4px}
.meth-h svg{width:7px;height:7px}
.txt ul{margin:2px 0 3px 8px}
.txt li{margin-bottom:.3px}

/* cover */
.cover-name{position:absolute;right:26px;top:220px;font-size:9.5px;font-weight:500;letter-spacing:.4px}
.cover-sub{position:absolute;right:22px;top:234px;font-size:6.3px;color:var(--olive)}
.cover-meta{position:absolute;right:26px;top:249px;font-size:4.4px;line-height:1.95;text-align:right;color:#555}
.cover-meta b{color:#111;font-weight:700}
.cover-vline{position:absolute;right:22px;top:248px;width:.6px;height:36px;background:var(--olive)}
.cover-brand{position:absolute;left:132px;top:172px;width:80px;text-align:center}
.cover-brand .mark{width:24px;height:24px;border-radius:50%;background:#3a3f3a;margin:0 auto 2px;border:1px solid #ddd}
.cover-brand .name{font-size:8.4px;font-weight:700;color:var(--olive)}

/* last page */
.back-brand{position:absolute;left:102px;top:68px;width:90px;text-align:center}
.back-brand .mark{width:22px;height:22px;border-radius:50%;background:#3a3f3a;margin:0 auto 2px;border:1px solid #ddd}
.back-brand .name{font-size:8.8px;font-weight:700;color:var(--olive)}
.url{position:absolute;top:262px;width:100%;text-align:center;color:#fff;font-size:5px;letter-spacing:2.3px}
</style>
</head>
<body>
<div class="board">

<!-- 1 cover -->
<section class="page c1 r1 cover">
  <svg width="226" height="293" viewBox="0 0 226 293" style="position:absolute;left:0;top:0">
    <defs>
      <linearGradient id="coverBg" x1="0" y1="0" x2="1" y2="1">
        <stop offset="0" stop-color="#0b0f14"/><stop offset=".55" stop-color="#17242e"/><stop offset="1" stop-color="#0a0c0f"/>
      </linearGradient>
    </defs>
    <rect width="226" height="293" fill="url(#coverBg)" role="img" aria-label="Dark cyber security artwork with fingerprint and network icons"/>
    <path d="M0 268 L155 168 Q168 160 180 168 L226 210 L226 293 L0 293 Z" fill="#fff"/>
    <path d="M0 262 L153 164 Q168 154 183 164 L226 202" fill="none" stroke="#9db548" stroke-width="2"/>
    <path d="M0 280 L120 205" fill="none" stroke="#9db548" stroke-width=".7"/>
  </svg>
  <div class="cover-brand"><div class="mark"></div><div class="name">Vantage Breach</div></div>
  <div class="cover-name">Example Client Name</div>
  <div class="cover-sub">Penetration Test Engagement Report</div>
  <div class="cover-meta">This Report Created for: <b>Client Name Here</b><br>Engagement Date: <b>7 Feb 2021</b><br>Testing Performed by: <b>Company Name Here</b></div>
  <div class="cover-vline"></div>
</section>

<!-- 2 confidential -->
<section class="page c2 r1">
  <div class="stop">STOP!</div>
  <div class="conf">THIS REPORT IS CONFIDENTIAL</div>
  <div class="conf-txt">
    <p>This report contains <em>Sensitive Information</em> about Client Name Here and should be classified at their <em>Highest Sensitivity Level</em>. Only those individuals that have a valid need to know should be allowed access to this report. Distribution should be limited to electronic formats which have password protection capabilities. Unauthorized viewing, distribution, or use of this report is prohibited.</p>
    <p>If you have found this report, <em>Secure It</em> until you are able to deliver it to the appropriate personnel.</p>
  </div>
  <div class="mini-brand"><div class="mark"></div><div class="name">Vantage Breach</div></div>
</section>

<!-- 3 toc -->
<section class="page c3 r1">
  <div class="toc-rule"></div>
  <div class="toc-head">Table <span>of</span><br><span>Content</span></div>
  <ul class="toc">
    <li>EXECUTIVE SUMMARY<span class="d"></span>4</li>
    <li>SCOPE<span class="d"></span>4</li>
    <li>ASSESSMENT OBJECTIVES<span class="d"></span>5</li>
    <li>RISK AND EXPLOITS DEFINITIONS<span class="d"></span>5</li>
    <li>FINDINGS AND RECOMMENDATIONS OVERVIEW<span class="d"></span>6</li>
    <li>POSITIVE OBSERVATIONS<span class="d"></span>7</li>
    <li>FINDINGS DETAILS<span class="d"></span>7</li>
    <li>CRITICAL RISK FINDINGS<span class="d"></span>8</li>
    <li class="sub">C1 - Test Critical Risk Finding<span class="d"></span>8</li>
    <li>HIGH RISK FINDINGS<span class="d"></span>8</li>
    <li class="sub">H1 - Test High Risk Finding<span class="d"></span>8</li>
    <li>MEDIUM RISK FINDINGS<span class="d"></span>9</li>
    <li class="sub">M1 - Test Medium Risk Finding<span class="d"></span>9</li>
    <li>LOW RISK FINDINGS<span class="d"></span>9</li>
    <li class="sub">L1 - Test Low Risk Finding<span class="d"></span>9</li>
    <li>INFORMATIONAL FINDINGS<span class="d"></span>10</li>
    <li class="sub">I1 - Test Informational Finding<span class="d"></span>10</li>
    <li>EXPLOITATION<span class="d"></span>10</li>
    <li class="sub2">E1 – Exploit Name Here<span class="d"></span>10</li>
    <li>APPENDIX A: METHODOLOGIES<span class="d"></span>11</li>
    <li class="sub">External Network Penetration Testing<span class="d"></span>11</li>
    <li class="sub">Internal Network Penetration Testing<span class="d"></span>13</li>
    <li class="sub">Web Application Penetration Testing<span class="d"></span>14</li>
  </ul>
</section>

<!-- 4 executive summary -->
<section class="page c4 r1">
  <div class="photo" style="left:27px;top:25px;width:199px;height:108px;background:linear-gradient(135deg,#3a4046,#6c7176 55%,#2b2f33)" role="img" aria-label="Photo of hands working at a laptop with notes"></div>
  <div class="hbox" style="left:31px;top:122px">EXECUTIVE<br><span>SUMMARY</span></div>
  <div class="txt" style="top:144px">
    <p>Penetration and vulnerability testing began with an information-gathering interview between Company Name Here and Client Name Here's IT department personnel. The interview gave the testers a full understanding of the client's asset infrastructure and the best opportunity for choosing a suitable initial approach. It also served as a venue to discuss specific vulnerability concerns. Once the scope of testing was agreed upon, the client granted the testers latitude and autonomy while conducting tests. This approach produces a more organic process of discovery and will often result in a greater number of findings. All testing was conducted within the agreed scope and in line with industry standards and best practices.</p>
    <p>This section is intended to be used as an overview. Details have been left out in order to allow the executive level reader to quickly assess what was done, how severe the findings are, and what an appropriate response should look like. Detailed findings, with their proofs and suggested solutions, can be found in section four of this report.</p>
  </div>
  <div class="hbox" style="left:31px;top:215px">Scope</div>
  <div class="txt" style="top:228px">
    <p>On Engagement Date Here Company Name Here conducted a series of security tests (referred to as engagements) of Client Name Here's information systems. Engagements are generally organic in nature and often overlap as weaknesses are found, exploited, and then leveraged to further compromise parts of the target systems or network.</p>
    <p>At the request of Client Name Here, Company Name Here conducted a security assessment from 1/1/2000 to 2/2/2000, for the host(s)/range(s).</p>
  </div>
  <svg class="foot" viewBox="0 0 226 60"><path d="M100 58 L168 16 Q176 11 184 17 L226 50" fill="none" stroke="#9db548" stroke-width="1"/></svg>
  <div class="pnum">4</div>
  <div class="brand"><div class="mark"></div><div class="name">Vantage Breach</div></div>
</section>

<!-- 5 objectives -->
<section class="page c5 r1">
  <div class="hbox" style="left:31px;top:34px">Assessment <span>Objectives</span></div>
  <div class="txt" style="top:47px">
    <p>The purpose of a Penetration Test is to assess Client Name Here's information security posture and resilience to cyber-attacks. Company Name Here analyzes the available devices, hosts and applications, probing the hosts for weaknesses and exploiting the most vulnerable ones. If an attack leads to a breach, the testers probe further network resources and exploit the most susceptible devices.</p>
    <p>The following table lists the categorized findings and associated risk ratings for this assessment. It allows Client Name Here to quickly judge the level of risk and prioritize remediation efforts.</p>
  </div>
  <table class="tbl-sum">
    <tr><th style="text-align:left">b</th><th></th><th>Total</th><th>Open Findings</th><th>Closed Findings</th></tr>
    <tr><td>Critical Risk</td><td><span class="sw" style="background:var(--critical)"></span></td><td>1</td><td>1</td><td>0</td></tr>
    <tr><td>High Risk</td><td><span class="sw" style="background:var(--high)"></span></td><td>2</td><td>2</td><td>0</td></tr>
    <tr><td>Medium Risk</td><td><span class="sw" style="background:var(--medium)"></span></td><td>3</td><td>3</td><td>0</td></tr>
    <tr><td>Low Risk</td><td><span class="sw" style="background:var(--low)"></span></td><td>4</td><td>4</td><td>0</td></tr>
    <tr><td>Informational</td><td><span class="sw" style="background:var(--info)"></span></td><td>5</td><td>5</td><td>0</td></tr>
  </table>
  <div class="hbox" style="left:31px;top:126px">Risk and Exploits <span>Definitions</span></div>
  <div class="txt" style="top:139px">
    <p>The risk associated with each finding is calculated using the Common Vulnerability Scoring System (CVSS). The CVSS assigns a severity score to each weakness, which is an assessment of the priority with which each risk will be viewed.</p>
  </div>
  <table class="tbl-def">
    <tr><th>Risk Rating</th><th>Definition</th></tr>
    <tr><td><span class="sw" style="background:var(--critical)"></span> Critical Risk</td><td>Exploitation of the technical or procedural weakness will cause substantial harm to business processes. Serious political, financial and legal damage is likely to result.</td></tr>
    <tr><td><span class="sw" style="background:var(--high)"></span> High Risk</td><td>Exploitation of the technical or procedural weakness will cause substantial harm to business processes. Significant political, financial and legal damage is likely to result.</td></tr>
    <tr><td><span class="sw" style="background:var(--medium)"></span> Medium Risk</td><td>Exploitation of the weakness will significantly impact confidentiality, integrity and/or availability of the system or data. Moderate financial loss or public embarrassment may result.</td></tr>
    <tr><td><span class="sw" style="background:var(--low)"></span> Low Risk</td><td>Exploitation of these weaknesses will cause minimal impact to operations. The information may also be at risk, causing slight financial loss or public embarrassment.</td></tr>
    <tr><td><span class="sw" style="background:var(--info)"></span> Informational</td><td>These findings are observations noted during the assessment that do not equate to a weakness.</td></tr>
    <tr><td><span class="sw" style="background:#111"></span> Exploits</td><td>Exploits are techniques used in order to gain unauthorized access to a given information resource or system.</td></tr>
  </table>
  <svg class="foot" viewBox="0 0 226 60"><path d="M100 58 L168 16 Q176 11 184 17 L226 50" fill="none" stroke="#9db548" stroke-width="1"/></svg>
  <div class="pnum">5</div>
  <div class="brand"><div class="mark"></div><div class="name">Vantage Breach</div></div>
</section>

<!-- 6 findings overview -->
<section class="page c1 r2">
  <div class="photo" style="left:26px;top:23px;width:200px;height:121px;background:linear-gradient(135deg,#5c646b,#a7adb1 45%,#3d4348)" role="img" aria-label="Photo of a laptop showing a data dashboard"></div>
  <div class="hbox" style="left:31px;top:124px">Findings and Recommendations<br><span>Overview</span></div>
  <div class="txt" style="top:148px">
    <p><b>Implement and enforce change control across all information systems:</b> Company Name Here found misconfiguration and insecure deployment issues across the various systems. The weaknesses that arose can be reduced by using change control processes on all information systems.</p>
    <p><b>Implement regular reviews of firewall rule set:</b> Client Name Here should regularly review the firewall rules to ensure that all systems and applications open to internet traffic still have a business need or justification to exist. Follow NIST SP 800-41 guidance on firewall implementation, configuration and testing.</p>
    <p><b>Implement a patch management program:</b> Operating a strong patch management program per NIST SP 800-40 is an important part of keeping a proper security posture. This helps the client reduce the risk that results from running unpatched services.</p>
    <p><b>Conduct regular penetration tests and vulnerability assessments:</b> As part of an effective organizational risk management strategy, penetration tests and vulnerability assessments should be conducted on a regular basis. Doing so will allow the client to determine whether current security controls are installed properly, operating as intended, and producing the desired outcome for confidentiality, integrity and availability of its information systems.</p>
    <p><b>Restrict network access to server management interfaces:</b> Proper network segmentation will reduce exposure to internal attacks against the server environment. A well-designed DMZ lets the client conduct its business in a way that does not expose internal information systems to attack. Consult FIPS 191 for guidance.</p>
  </div>
  <svg class="foot" viewBox="0 0 226 60"><path d="M100 58 L168 16 Q176 11 184 17 L226 50" fill="none" stroke="#9db548" stroke-width="1"/></svg>
  <div class="bar"></div>
  <div class="pnum">6</div>
  <div class="brand"><div class="mark"></div><div class="name">Vantage Breach</div></div>
</section>

<!-- 7 positive observations -->
<section class="page c2 r2">
  <div class="photo" style="left:26px;top:28px;width:200px;height:134px;background:linear-gradient(135deg,#1d2a3c,#36506e 50%,#101722)" role="img" aria-label="Photo of source code on a laptop screen"></div>
  <div class="hbox" style="left:31px;top:152px">Positive<br><span>Observations</span></div>
  <div class="txt" style="top:175px">
    <p><b>Strong patch management:</b> Company Name Here found that very few systems lack up-to-date patches, which shows that effective patch management processes are being followed and are effective.</p>
    <p><b>Hardened information systems:</b> Client Name Here has implemented strong defense in depth practices that make it very difficult for an attacker to gain access to an information system.</p>
  </div>
  <div class="hbox" style="left:31px;top:202px">Findings <span>Details</span></div>
  <div class="txt" style="top:214px">
    <p>This section lists the weaknesses discovered during the engagement(s). The individual findings are categorized by severity (Critical, High, Medium, Low, and Informational) and are listed under the matching subheading. The results of each finding are presented in table format for consistency and ease of use. The top row of each table is labeled with a sequential reference number and colour-coded for easy reference and navigation. Each table gives the name of the weakness, whether it led to exploitation, which systems are affected, a brief description, the evidence (usually a screen shot), and a recommended remediation strategy.</p>
  </div>
  <svg class="foot" viewBox="0 0 226 60"><path d="M100 58 L168 16 Q176 11 184 17 L226 50" fill="none" stroke="#9db548" stroke-width="1"/></svg>
  <div class="bar"></div>
  <div class="pnum">7</div>
  <div class="brand"><div class="mark"></div><div class="name">Vantage Breach</div></div>
</section>

<!-- 8 critical & high -->
<section class="page c3 r2">
  <div class="find" style="top:30px">
    <div class="hbox">Critical Risk <span>Findings</span></div>
    <div class="sub"><i style="color:var(--critical)">C1</i> - Test Critical Risk Finding</div>
    <div class="rule" style="background:var(--critical)"></div>
    <div class="row"><b>Exploited:</b> No</div>
    <div class="row"><b>Affected Systems:</b> <a>https://testing.com/injecthere.php?vuln=test</a></div>
    <div class="row"><b>Description:</b><br>Command injection flaws occur when an application passes user-supplied input to a system shell without proper validation. An attacker can append extra commands that run with the privileges of the application, which may lead to full compromise of the host and access to sensitive data stored on the server. Impact depends on the security context of the running service and the privileges it holds on the host.</div>
    <div class="row"><b>Evidence:</b> The following screenshot shows the command injection weakness.</div>
    <div class="row"><b>Recommendation:</b><br>Avoid passing user input to operating system commands. Where this cannot be avoided, apply strict allow-list validation and use safer platform functions that cannot be manipulated to run extra commands.</div>
  </div>
  <div class="find" style="top:146px">
    <div class="hbox">High Risk <span>Findings</span></div>
    <div class="sub"><i style="color:var(--high)">H1</i> - Test High Risk Finding</div>
    <div class="rule" style="background:var(--high)"></div>
    <div class="row"><b>Exploited:</b> No</div>
    <div class="row"><b>Affected Systems:</b> <a>https://testing.com/injecthere.php?vuln=test</a></div>
    <div class="row"><b>Description:</b><br>Command injection flaws occur when an application passes user-supplied input to a system shell without proper validation. An attacker can append extra commands that run with the privileges of the application, which may lead to full compromise of the host and access to sensitive data stored on the server. Impact depends on the security context of the running service and the privileges it holds on the host.</div>
    <div class="row"><b>Evidence:</b> The following screenshot shows the command injection weakness.</div>
    <div class="row"><b>Recommendation:</b><br>Avoid passing user input to operating system commands. Where this cannot be avoided, apply strict allow-list validation and use safer platform functions that cannot be manipulated to run extra commands.</div>
  </div>
  <svg class="foot" viewBox="0 0 226 60"><path d="M100 58 L168 16 Q176 11 184 17 L226 50" fill="none" stroke="#9db548" stroke-width="1"/></svg>
  <div class="bar"></div>
  <div class="pnum">8</div>
  <div class="brand"><div class="mark"></div><div class="name">Vantage Breach</div></div>
</section>

<!-- 9 medium & low -->
<section class="page c4 r2">
  <div class="find" style="top:29px">
    <div class="hbox">Medium Risk <span>Findings</span></div>
    <div class="sub"><i style="color:var(--medium)">M1</i> - Test Medium Risk Finding</div>
    <div class="rule" style="background:var(--medium)"></div>
    <div class="row"><b>Exploited:</b> No</div>
    <div class="row"><b>Affected Systems:</b> <a>https://testing.com/injecthere.php?vuln=test</a></div>
    <div class="row"><b>Description:</b><br>Command injection flaws occur when an application passes user-supplied input to a system shell without proper validation. An attacker can append extra commands that run with the privileges of the application, which may lead to full compromise of the host and access to sensitive data stored on the server. Impact depends on the security context of the running service and the privileges it holds on the host.</div>
    <div class="row"><b>Evidence:</b> The following screenshot shows the command injection weakness.</div>
    <div class="row"><b>Recommendation:</b><br>Avoid passing user input to operating system commands. Where this cannot be avoided, apply strict allow-list validation and use safer platform functions that cannot be manipulated to run extra commands.</div>
  </div>
  <div class="find" style="top:146px">
    <div class="hbox">Low Risk <span>Findings</span></div>
    <div class="sub"><i style="color:var(--low)">L1</i> - Test Low Risk Finding</div>
    <div class="rule" style="background:var(--low)"></div>
    <div class="row"><b>Exploited:</b> No</div>
    <div class="row"><b>Affected Systems:</b> <a>https://testing.com/injecthere.php?vuln=test</a></div>
    <div class="row"><b>Description:</b><br>Command injection flaws occur when an application passes user-supplied input to a system shell without proper validation. An attacker can append extra commands that run with the privileges of the application, which may lead to full compromise of the host and access to sensitive data stored on the server. Impact depends on the security context of the running service and the privileges it holds on the host.</div>
    <div class="row"><b>Evidence:</b> The following screenshot shows the command injection weakness.</div>
    <div class="row"><b>Recommendation:</b><br>Avoid passing user input to operating system commands. Where this cannot be avoided, apply strict allow-list validation and use safer platform functions that cannot be manipulated to run extra commands.</div>
    <div class="end" style="background:var(--low)"></div>
  </div>
  <svg class="foot" viewBox="0 0 226 60"><path d="M100 58 L168 16 Q176 11 184 17 L226 50" fill="none" stroke="#9db548" stroke-width="1"/></svg>
  <div class="bar"></div>
  <div class="pnum">9</div>
  <div class="brand"><div class="mark"></div><div class="name">Vantage Breach</div></div>
</section>

<!-- 10 informational & exploitation -->
<section class="page c5 r2">
  <div class="find" style="top:33px">
    <div class="hbox">Informational <span>Findings</span></div>
    <div class="sub"><i style="color:var(--info)">I1</i> - Test Informational Finding</div>
    <div class="rule" style="background:var(--info)"></div>
    <div class="row"><b>Exploited:</b> No</div>
    <div class="row"><b>Affected Systems:</b> <a>https://testing.com/injecthere.php?vuln=test</a></div>
    <div class="row"><b>Description:</b><br>Command injection flaws occur when an application passes user-supplied input to a system shell without proper validation. An attacker can append extra commands that run with the privileges of the application, which may lead to full compromise of the host and access to sensitive data stored on the server. Impact depends on the security context of the running service and the privileges it holds on the host.</div>
    <div class="row"><b>Evidence:</b> The following screenshot shows the command injection weakness.</div>
    <div class="row"><b>Recommendation:</b><br>Avoid passing user input to operating system commands. Where this cannot be avoided, apply strict allow-list validation and use safer platform functions that cannot be manipulated to run extra commands.</div>
  </div>
  <div class="find" style="top:150px">
    <div class="hbox">Exploitation</div>
    <div class="sub">E1 – Exploit Name Here</div>
    <div class="rule" style="background:#222"></div>
    <div class="row" style="height:31px"><b>Applicable Findings:</b></div>
    <div class="row"><b>Affected Systems:</b> 10.1.1.1, 10.1.1.2, 10.1.1.3</div>
    <div class="row"><b>Exploitation Walkthrough:</b><br>During the assessment, the testers found that several systems were open to the MS17-010 (EternalBlue) flaw. This allowed the team to gain full privileged shell access to the system as the NT Authority / SYSTEM user. The screenshot below shows the flaw being exploited and an advanced interactive shell gained on the host.</div>
  </div>
  <svg class="foot" viewBox="0 0 226 60"><path d="M100 58 L168 16 Q176 11 184 17 L226 50" fill="none" stroke="#9db548" stroke-width="1"/></svg>
  <div class="bar"></div>
  <div class="pnum">10</div>
  <div class="brand"><div class="mark"></div><div class="name">Vantage Breach</div></div>
</section>

<!-- 11 appendix -->
<section class="page c1 r3">
  <div class="photo" style="left:26px;top:34px;width:200px;height:133px;background:linear-gradient(135deg,#6e757b,#b8bcbf 50%,#4a5055)" role="img" aria-label="Photo of a laptop with code on a desk"></div>
  <div class="hbox" style="left:35px;top:158px">Appendix A:<br><span>Methodologies</span></div>
  <div class="meth-h" style="top:188px"><svg viewBox="0 0 10 10"><path d="M5 .5 L9 2 V5 Q9 8.5 5 9.5 Q1 8.5 1 5 V2 Z" fill="#222"/></svg>External Network Penetration Testing</div>
  <div class="txt" style="top:199px">
    <p>The team follows an in-house developed methodology based on the Penetration Testing Execution Standard (PTES). At a high-level, our methodology is executed over the following phases:</p>
    <ul>
      <li>Open source Intelligence Information Gathering (OSINT)</li>
      <li>Discovery and Enumeration</li>
      <li>Vulnerability Scanning and Analysis</li>
      <li>Vulnerability Exploitation</li>
      <li>Post Exploitation Activities</li>
      <li>Report Development</li>
      <li>Post Engagement Consulting</li>
    </ul>
  </div>
  <svg class="foot" viewBox="0 0 226 60"><path d="M100 58 L168 16 Q176 11 184 17 L226 50" fill="none" stroke="#9db548" stroke-width="1"/></svg>
  <div class="bar"></div>
  <div class="pnum">11</div>
  <div class="brand"><div class="mark"></div><div class="name">Vantage Breach</div></div>
</section>

<!-- 12 external phases -->
<section class="page c2 r3">
  <div class="txt" style="top:30px">
    <p><b>Phase 1: Opensource Intelligence Information Gathering (OSINT)</b><br>Phase 1 begins with gathering information via open source resources. These include search engines, online metadata gathering tools, domain registrants, whois records and more. This phase is designed for discovery, to find the presence of weaknesses and exposure, all while remaining fully stealthy.</p>
    <p><b>Phase 2: Discovery and Enumeration</b><br>Phase 2 involves actual packets being sent to the network to discover live systems and any open ports and services exposed to the external network. This gives the tester a view of possible applications and high level weaknesses that may affect those hosts. This phase also involves enumeration of banners and application version strings that may lead to clues on weaknesses affecting the host.</p>
    <p><b>Phase 3: Vulnerability Scanning and Analysis</b><br>Phase 3 involves automated and manual testing of the target hosts and services found during phase 2. This phase uses multiple open source and commercial tools to automatically analyze the presence of known weaknesses in the information system and exposed services. Manual analysis is then done to flush out false positives and find weaknesses that automation may have missed.</p>
    <p><b>Phase 4: Vulnerability Exploitation</b><br>Phase 4 involves the exploitation of weaknesses found in phase 3. During this phase denial of service conditions and weaknesses are NOT exploited but are documented in phase 6. Careful analysis and exploitation are performed using manual techniques and very little automation in order to achieve initial access to the target(s).</p>
    <p><b>Phase 5: Post Exploitation Activities</b><br>Phase 5 involves the tactics and procedures to further gain access into the environment. This may include privilege escalation, lateral movement, additional enumeration, scanning and exploitation as outlined in phases 2-4, with key objectives that may include obtaining domain or enterprise admin privileges.</p>
    <p><b>Phase 6: Report Development</b><br>Phase 6 is where the engagement deliverables are developed and additional testing may occur to ensure proper evidence has been captured in order to prove risks and exposures of the network environment. Deliverables are commonly in the form of report documents, slide decks or letters of attestation.</p>
    <p><b>Phase 7: Post Engagement Consulting</b><br>Phase 7 involves the consultant(s) performing a walkthrough of the engagement deliverables and answering any question about the engagement and next steps. Client feedback is noted and adjustments made to the final deliverable(s).</p>
  </div>
  <svg class="foot" viewBox="0 0 226 60"><path d="M100 58 L168 16 Q176 11 184 17 L226 50" fill="none" stroke="#9db548" stroke-width="1"/></svg>
  <div class="bar"></div>
  <div class="pnum">12</div>
  <div class="brand"><div class="mark"></div><div class="name">Vantage Breach</div></div>
</section>

<!-- 13 internal -->
<section class="page c3 r3">
  <div class="meth-h" style="top:31px"><svg viewBox="0 0 10 10"><g stroke="#222" stroke-width=".8"><line x1="5" y1="5" x2="1" y2="1"/><line x1="5" y1="5" x2="9" y2="1.5"/><line x1="5" y1="5" x2="2" y2="9"/><line x1="5" y1="5" x2="8.5" y2="8.5"/></g><circle cx="5" cy="5" r="1.6" fill="#222"/></svg>Internal Network Penetration Testing</div>
  <div class="txt" style="top:42px">
    <p>The team follows an in-house developed methodology based on the Penetration Testing Execution Standard (PTES). At a high-level, our methodology is executed over the following phases:</p>
    <ul>
      <li>Discovery and Enumeration</li>
      <li>Vulnerability Scanning and Analysis</li>
      <li>Vulnerability Exploitation</li>
      <li>Post Exploitation Activities</li>
      <li>Report Development</li>
      <li>Post Engagement Consulting</li>
    </ul>
    <p><b>Phase 1: Discovery and Enumeration</b><br>Phase 1 involves actual packets being sent to the network to discover live systems and any open ports and services exposed on the internal network. This gives the tester a view of possible applications and high level weaknesses that may affect those hosts. This phase also involves enumeration of banners and application version strings that may lead to clues on weaknesses affecting the host.</p>
    <p><b>Phase 2: Vulnerability Scanning and Analysis</b><br>Phase 2 involves automated and manual testing of the target hosts and services found during phase 1. Multiple open source and commercial tools are used to analyze the presence of known weaknesses. Manual analysis then flushes out false positives and finds weaknesses that can only be discerned through human intelligence.</p>
    <p><b>Phase 3: Vulnerability Exploitation</b><br>Phase 3 involves the exploitation of weaknesses found in phase 2. Denial of service conditions are NOT exploited but are documented in phase 5. Careful analysis and exploitation are performed using manual techniques in order to achieve initial access to the target(s).</p>
    <p><b>Phase 4: Post Exploitation Activities</b><br>Phase 4 involves the tactics and procedures to further gain access into the environment, such as privilege escalation, lateral movement, additional enumeration and exploitation as outlined in phases 1-3, with key objectives that may include obtaining domain admin privileges.</p>
    <p><b>Phase 5: Report Development</b><br>Phase 5 is where the engagement deliverables are developed and additional testing may occur to ensure proper evidence has been captured in order to prove risks and exposures of the network environment.</p>
    <p><b>Phase 6: Post Engagement Consulting</b><br>Phase 6 involves the consultant(s) performing a walkthrough of the engagement deliverables and answering any question about next steps. Client feedback is noted and adjustments made to the final deliverable(s).</p>
  </div>
  <svg class="foot" viewBox="0 0 226 60"><path d="M100 58 L168 16 Q176 11 184 17 L226 50" fill="none" stroke="#9db548" stroke-width="1"/></svg>
  <div class="bar"></div>
  <div class="pnum">13</div>
  <div class="brand"><div class="mark"></div><div class="name">Vantage Breach</div></div>
</section>

<!-- 14 web application -->
<section class="page c4 r3">
  <div class="meth-h" style="top:30px"><svg viewBox="0 0 10 10"><circle cx="5" cy="5" r="4.2" fill="none" stroke="#222" stroke-width=".8"/><ellipse cx="5" cy="5" rx="1.8" ry="4.2" fill="none" stroke="#222" stroke-width=".6"/><line x1=".8" y1="5" x2="9.2" y2="5" stroke="#222" stroke-width=".6"/></svg>Web Application Penetration Testing</div>
  <div class="txt" style="top:41px">
    <p>The team follows an in-house developed methodology based on the Open Web Application Security Project (OWASP) testing guide. At a high-level, our methodology is executed over the following phases:</p>
    <ul>
      <li>Recon and Mapping</li>
      <li>Vulnerability Discovery</li>
      <li>Vulnerability Exploitation</li>
      <li>Post Exploitation Activities</li>
      <li>Report Development</li>
      <li>Post Engagement Consulting</li>
    </ul>
    <p><b>Phase 1: Recon and Mapping</b><br>Phase 1 begins with gathering information via open source resources such as search engines, metadata gathering tools, domain registrants and more. During this phase we also map the target application by spending time getting to know all of its functionality, clicking on every link and submitting every request. Relationships between the application components are analyzed to determine how all functionalities fit together.</p>
    <p><b>Phase 2: Vulnerability Discovery</b><br>Phase 2 involves automated and manual testing of the target application based on the content found in phase 1. Automated scanning and fuzzing of each parameter is done during the discovery phase to help the tester find known and unknown weaknesses. Manual analysis is also done against the logic and overall design of the application, since some issues are only discoverable through human intelligence.</p>
    <p><b>Phase 3: Vulnerability Exploitation</b><br>Phase 3 involves the exploitation of weaknesses found in phase 2. Denial of service conditions are NOT exploited but are documented in phase 5. Careful analysis and exploitation are performed using manual techniques and very little automation.</p>
    <p><b>Phase 4: Post Exploitation Activities</b><br>Phase 4 involves the tactics and procedures to further gain access into the environment, such as privilege escalation, lateral movement, additional enumeration and exploitation as outlined in phases 1-3.</p>
    <p><b>Phase 5: Report Development</b><br>Phase 5 is where the engagement deliverables are developed and additional testing may occur to ensure proper evidence has been captured to prove risks and exposures of the application(s).</p>
    <p><b>Phase 6: Post Engagement Consulting</b><br>Phase 6 involves the consultant(s) performing a walkthrough of the engagement deliverables and answering any question about next steps. Client feedback is noted and adjustments made to the final deliverable(s).</p>
  </div>
  <svg class="foot" viewBox="0 0 226 60"><path d="M100 58 L168 16 Q176 11 184 17 L226 50" fill="none" stroke="#9db548" stroke-width="1"/></svg>
  <div class="bar"></div>
  <div class="pnum">14</div>
  <div class="brand"><div class="mark"></div><div class="name">Vantage Breach</div></div>
</section>

<!-- 15 back cover -->
<section class="page c5 r3">
  <svg width="226" height="293" viewBox="0 0 226 293" style="position:absolute;left:0;top:0">
    <defs>
      <linearGradient id="backBg" x1="0" y1="0" x2="1" y2="1">
        <stop offset="0" stop-color="#1a201c"/><stop offset=".6" stop-color="#2e3b2a"/><stop offset="1" stop-color="#0c0f0d"/>
      </linearGradient>
    </defs>
    <rect width="226" height="293" fill="url(#backBg)" role="img" aria-label="Dark photo of a laptop with green code streaming on screen"/>
    <path d="M0 0 H226 V148 Q226 178 196 178 H160 Q140 178 124 166 L0 74 Z" fill="#fff"/>
    <path d="M0 80 L122 172 Q140 185 162 185 H196 Q226 185 226 150" fill="none" stroke="#9db548" stroke-width="1.3"/>
    <path d="M0 44 L30 66" fill="none" stroke="#9db548" stroke-width=".8"/>
  </svg>
  <div class="back-brand"><div class="mark"></div><div class="name">Vantage Breach</div></div>
  <div class="url">www.vantage-breach.com</div>
</section>

</div>
</body>
</html>
```